Refresh of a Media Kit for Adtech Company - Needs jazzing up!

We have a Media Kit that's too ugly and boring to send to clients. Attaching some examples of ones we like better. Keep the general styling and theme of the current media kit (it's our brand style) and all the information conveyed, but please change anything and everything else to make it more dynamic. Attaching examples of media kits we like.

The "Media Kit Vexa" is the one you're designing, the others are just examples of media kits we liked.
Updates

Here's a link to "Glamour Shots" that can be used as appropriate throughout the Media kit: https://www.filecrate-example.com/sh/k8trw21mzpq4xnb/QXP7Lmv3bRw8_TzKe4jHsUcYd?dl=0

Target Market(s)

Demand partners

Colors
0592cd
85cae6
34a7d8

Requirements
Nice to have
• Here are some glamour shots you can use if you see a good fit for any of them: https://www.filecrate-example.com/sh/k8trw21mzpq4xnb/QXP7Lmv3bRw8_TzKe4jHsUcYd?dl=0

```html
<!DOCTYPE html>
<html lang="en">
<head>
<meta charset="utf-8">
<title>DOOH Now – Inventory Highlights</title>
<link href="https://fonts.googleapis.com/css2?family=Roboto:wght@300;400;700&display=swap" rel="stylesheet">
<style>
  :root{
    --page-bg:#e6e6e6;
    --slide-bg:#ffffff;
    --brand-deep:#0592cd;
    --brand-mid:#34a7d8;
    --brand-light:#85cae6;
    --kicker:#5bb8e6;
    --icon-blue:#1b8fe6;
    --ink:#2b2b2b;
    --label:#4a4a4a;
    --muted-disc:#e4e4e4;
    --page-number:#9a9a9a;
  }
  *{box-sizing:border-box;margin:0;padding:0}
  html,body{width:1200px;height:724px;overflow:hidden}
  body{background:var(--page-bg);font-family:'Roboto',Arial,sans-serif;position:relative;color:var(--ink)}

  .slide{position:absolute;width:544px;height:306px;background:var(--slide-bg);overflow:hidden}
  .slide--clinics{left:39px;top:40px}
  .slide--imaging{left:617px;top:40px}
  .slide--records{left:39px;top:378px}
  .slide--grocery{left:617px;top:378px}

  .heading{position:absolute;top:30px;width:240px}
  .slide--clinics .heading,.slide--records .heading{left:27px}
  .slide--imaging .heading,.slide--grocery .heading{left:315px}
  .heading__kicker{font-size:17.5px;font-weight:700;color:var(--kicker);letter-spacing:.2px;line-height:20px}
  .heading__title{font-size:18.5px;font-weight:300;line-height:23.5px;margin-top:3px;color:var(--ink)}
  .heading__title b{font-weight:700}

  .photo{position:absolute;top:0;height:306px}
  .photo--right{left:253px;width:291px;border-radius:62px 0 0 62px/80px 0 0 80px}
  .photo--left{left:0;width:289px;border-radius:0 62px 62px 0/0 80px 80px 0}
  .photo--clinic{background:linear-gradient(135deg,#b89a72 0%,#ece7de 35%,#f4f1ea 60%,#c8b08a 100%)}
  .photo--imaging{background:linear-gradient(120deg,#e9eef3 0%,#cfd6de 40%,#f5f7f9 65%,#1d3b7a 100%)}
  .photo--records{background:linear-gradient(120deg,#2a1e1c 0%,#6b3a2f 35%,#b7a08b 65%,#3b4d6e 100%)}
  .photo--grocery{background:linear-gradient(110deg,#2e3346 0%,#4b4f63 40%,#eef2f6 62%,#c23a34 100%)}

  .feature-badge{position:absolute;width:70px;height:70px;border-radius:50%;background:var(--brand-light);
    color:#fff;opacity:.97;text-align:center;font-size:8.5px;font-weight:300;line-height:10px;padding-top:10px}
  .feature-badge svg{display:block;margin:0 auto 3px}
  .slide--clinics .feature-badge,.slide--records .feature-badge{left:220px}
  .slide--imaging .feature-badge,.slide--grocery .feature-badge{left:254px}
  .slide--clinics .feature-badge,.slide--imaging .feature-badge{top:120px}
  .slide--records .feature-badge,.slide--grocery .feature-badge{top:119px}

  .stat{position:absolute;width:90px;text-align:center;transform:translateX(-50%)}
  .stat__icon{display:block;margin:0 auto;border-radius:50%;background:var(--icon-blue)}
  .stat__label{display:block;font-size:7.3px;font-weight:400;line-height:9px;color:var(--label);margin-top:4px}
  .stat--exclusive .stat__icon{background:var(--muted-disc)}
  .exclusive-text{position:absolute;left:0;right:0;top:50%;transform:translateY(-50%) rotate(-32deg);
    font-size:8px;font-weight:300;line-height:9.5px;color:#fff;text-align:center}

  .brand-name{position:absolute;right:12px;bottom:8px;font-size:8px;font-weight:400;letter-spacing:.3px}
  .brand-name--on-photo{color:#fff}
  .brand-name--on-white{color:var(--label)}

  .page-number{position:absolute;right:10px;bottom:4px;font-size:36px;font-weight:700;color:var(--page-number)}
</style>
</head>
<body>

<svg width="0" height="0" style="position:absolute">
  <defs>
    <symbol id="icon-expand" viewBox="0 0 40 40"><g fill="none" stroke="#fff" stroke-width="1.8" stroke-linecap="round"><path d="M11 15v-4h4M25 11h4v4M29 25v4h-4M15 29h-4v-4M11 11l6 6M29 11l-6 6M29 29l-6-6M11 29l6-6"/><rect x="17" y="17" width="6" height="6"/></g></symbol>
    <symbol id="icon-screen" viewBox="0 0 40 40"><g fill="none" stroke="#fff" stroke-width="1.8"><rect x="11" y="11" width="18" height="18" rx="1.5"/><path d="M18 16l6 4-6 4z" stroke-linejoin="round"/></g></symbol>
    <symbol id="icon-audience" viewBox="0 0 40 40"><g fill="none" stroke="#fff" stroke-width="1.8"><path d="M9 19c4-6 13-7 19-1"/><circle cx="18" cy="19" r="3.5"/><circle cx="24" cy="22" r="3"/><path d="M19 31c0-3.5 2.3-5 5-5s5 1.5 5 5z"/></g></symbol>
    <symbol id="icon-globe-pin" viewBox="0 0 40 40"><g fill="none" stroke="#fff" stroke-width="1.8"><path d="M20 31c-6-5-9-9-9-13a9 9 0 0 1 18 0c0 4-3 8-9 13z"/><circle cx="20" cy="18" r="5.5"/><path d="M17 15c2 1 1 3 3 3s1 3 3 2"/></g></symbol>
    <symbol id="icon-dwell" viewBox="0 0 40 40"><g fill="none" stroke="#fff" stroke-width="1.8" stroke-linecap="round"><circle cx="15" cy="12" r="2.5"/><path d="M14 16l1 7h6l3 6M12 18l-1 6 3 4h6"/><circle cx="26" cy="14" r="4.5"/><path d="M26 11.5v2.5h2"/></g></symbol>
    <symbol id="icon-income" viewBox="0 0 40 40"><g fill="none" stroke="#fff" stroke-width="1.8" stroke-linecap="round"><circle cx="14" cy="19" r="5"/><path d="M15.5 17h-2a1 1 0 0 0 0 2h1a1 1 0 0 1 0 2h-2M14 15.5v7"/><circle cx="25" cy="12" r="2.5"/><path d="M21 30v-9c0-3 8-3 8 0v9M25 22v8"/></g></symbol>
    <symbol id="icon-pill" viewBox="0 0 24 24"><g fill="none" stroke="#fff" stroke-width="1.4"><circle cx="8" cy="8" r="5"/><path d="M3.5 7h9M3.5 9.5h9"/><rect x="11" y="11" width="11" height="5.5" rx="2.75" transform="rotate(-40 16.5 13.75)"/></g></symbol>
    <symbol id="icon-purchase" viewBox="0 0 24 24"><g fill="none" stroke="#fff" stroke-width="1.4" stroke-linecap="round"><path d="M9 21c-4-3.5-6-6.5-6-9.5a6 6 0 0 1 12 0c0 3-2 6-6 9.5z"/><path d="M10.5 9h-2a1 1 0 0 0 0 2h1a1 1 0 0 1 0 2h-2M9 7.5v7M17 10h3M19 13v2M16 17h2M14 20h1"/></g></symbol>
  </defs>
</svg>

<section class="slide slide--clinics">
  <div class="heading">
    <p class="heading__kicker">DOOH NOW |</p>
    <h2 class="heading__title">Inventory Highlights –<br>Point of Care <b>Clinics</b></h2>
  </div>
  <div class="photo photo--right photo--clinic" role="img" aria-label="Bright clinic waiting room with armchairs and wall-mounted screen"></div>
  <div class="feature-badge"><svg width="26" height="26"><use href="#icon-pill"/></svg>Busy during<br>lockdown</div>

  <div class="stat" style="left:54px;top:130px"><svg class="stat__icon" width="40" height="40"><use href="#icon-expand"/></svg><span class="stat__label">Massive<br>scale</span></div>
  <div class="stat" style="left:109px;top:131px"><svg class="stat__icon" width="40" height="40"><use href="#icon-screen"/></svg><span class="stat__label">5000<br>screens</span></div>
  <div class="stat" style="left:162px;top:130px"><svg class="stat__icon" width="40" height="40"><use href="#icon-audience"/></svg><span class="stat__label">3M impressions<br>/month</span></div>
  <div class="stat" style="left:54px;top:204px"><svg class="stat__icon" width="40" height="40"><use href="#icon-globe-pin"/></svg><span class="stat__label">Nationwide</span></div>
  <div class="stat" style="left:109px;top:204px"><svg class="stat__icon" width="40" height="40"><use href="#icon-dwell"/></svg><span class="stat__label">College grads<br>high dwell time</span></div>
  <div class="stat stat--exclusive" style="left:167px;top:202px"><div style="position:relative;width:52px;height:52px;margin:0 auto"><span class="stat__icon" style="width:52px;height:52px"></span><span class="exclusive-text">Exclusive<br>to<br>AdCove</span></div></div>

  <div class="brand-name brand-name--on-photo">AdCove</div>
</section>

<section class="slide slide--imaging">
  <div class="photo photo--left photo--imaging" role="img" aria-label="Two doctors in white coats reviewing a document beside a hospital screen"></div>
  <div class="feature-badge"><svg width="26" height="26"><use href="#icon-pill"/></svg>Busy during<br>lockdown</div>
  <div class="heading">
    <p class="heading__kicker">DOOH NOW |</p>
    <h2 class="heading__title">Inventory Highlights –<br>Medical Imaging <b>Centers</b></h2>
  </div>

  <div class="stat" style="left:385px;top:131px"><svg class="stat__icon" width="50" height="50"><use href="#icon-screen"/></svg><span class="stat__label">50 screens</span></div>
  <div class="stat" style="left:461px;top:130px"><svg class="stat__icon" width="50" height="50"><use href="#icon-audience"/></svg><span class="stat__label">400k impressions/<br>month</span></div>
  <div class="stat stat--exclusive" style="left:347px;top:205px"><div style="position:relative;width:52px;height:52px;margin:0 auto"><span class="stat__icon" style="width:52px;height:52px"></span><span class="exclusive-text">Exclusive<br>to<br>AdCove</span></div></div>
  <div class="stat" style="left:422px;top:204px"><svg class="stat__icon" width="50" height="50"><use href="#icon-globe-pin"/></svg><span class="stat__label">Northeast U.S.</span></div>

  <div class="brand-name brand-name--on-white">AdCove</div>
</section>

<section class="slide slide--records">
  <div class="heading">
    <p class="heading__kicker">DOOH NOW |</p>
    <h2 class="heading__title">Inventory Highlights –<br>Urban Record <b>Stores</b></h2>
  </div>
  <div class="photo photo--right photo--records" role="img" aria-label="Shopper browsing vinyl records in a crowded record store"></div>
  <div class="feature-badge"><svg width="26" height="26"><use href="#icon-purchase"/></svg>Close to point<br>of purchase</div>

  <div class="stat" style="left:59px;top:129px"><svg class="stat__icon" width="49" height="49"><use href="#icon-screen"/></svg><span class="stat__label">X screens</span></div>
  <div class="stat" style="left:126px;top:128px"><svg class="stat__icon" width="49" height="49"><use href="#icon-audience"/></svg><span class="stat__label">X impressions<br>Per month</span></div>
  <div class="stat" style="left:59px;top:210px"><svg class="stat__icon" width="49" height="49"><use href="#icon-globe-pin"/></svg><span class="stat__label">Nationwide</span></div>
  <div class="stat" style="left:125px;top:210px"><svg class="stat__icon" width="49" height="49"><use href="#icon-income"/></svg><span class="stat__label">High income multiple<br>Visits/month</span></div>
  <div class="stat stat--exclusive" style="left:194px;top:207px"><div style="position:relative;width:52px;height:52px;margin:0 auto"><span class="stat__icon" style="width:52px;height:52px"></span><span class="exclusive-text">Exclusive<br>to<br>AdCove</span></div></div>

  <div class="brand-name brand-name--on-photo">AdCove</div>
</section>

<section class="slide slide--grocery">
  <div class="photo photo--left photo--grocery" role="img" aria-label="Store clerk beside a checkout screen showing grocery promotions"></div>
  <div class="feature-badge"><svg width="26" height="26"><use href="#icon-purchase"/></svg>Close to point<br>of purchase</div>
  <div class="heading">
    <p class="heading__kicker">DOOH NOW |</p>
    <h2 class="heading__title">Inventory Highlights –<br><b>Grocery</b></h2>
  </div>

  <div class="stat" style="left:385px;top:130px"><svg class="stat__icon" width="50" height="50"><use href="#icon-screen"/></svg><span class="stat__label">X screens</span></div>
  <div class="stat" style="left:461px;top:130px"><svg class="stat__icon" width="50" height="50"><use href="#icon-audience"/></svg><span class="stat__label">X impressions<br>per month</span></div>
  <div class="stat stat--exclusive" style="left:347px;top:206px"><div style="position:relative;width:52px;height:52px;margin:0 auto"><span class="stat__icon" style="width:52px;height:52px"></span><span class="exclusive-text">Exclusive<br>to<br>AdCove</span></div></div>
  <div class="stat" style="left:422px;top:205px"><svg class="stat__icon" width="50" height="50"><use href="#icon-globe-pin"/></svg><span class="stat__label">Northeast U.S.</span></div>

  <div class="brand-name brand-name--on-white">AdCove</div>
</section>

<div class="page-number">3</div>
</body>
</html>
```